Webdesign für Entwickler von onlinebasierten Terminformularen
Super Designs. Schnell und motiviert. Danke für die hervorragende Umsetzung und die Ideen!
Zielgruppe
Deutsch:
Wir sind ein Startup, das über die Seite Kalendrio.de zukünftig folgenden Service anbietet: Unternehmer können sehr flexibel (selbst) gestaltete Terminformulare erstellen und auf Ihrer Website einbinden. Kunden können dann diese Termine buchen und bekommen dann Erinnerungs-Mails und SMS.
Zielgruppe: Dienstleister wie Fotografen, Friseure, Versicherungsvertreter, Masseure, Restaurants, Arztpraxen. Also alle, die darauf angewiesen sind, dass vereinbarte Termine eingehalten werden und die die Terminvereinbarung vereinfachen wollen. Also weniger per Telefon, mehr über die eigene Website.
Englisch:
We are a start up, that is going to offer this services on the Website Kalendrio.de :
Companies can create highly flexible (self-designed) appointment forms and integrate them on their website. Customer can book appointments and will get an reminding email and SMS.
Target group: Service providers such as photographers, hairdressers, insurance agents, masseurs, restaurants, medical offices. So all those who depend on meeting agreed appointments and who want to simplify the appointment. Less by telephone, more over their own website.
Aufgabenstellung
Übersichtlichkeit, genug Weißraum, deutliche, große Überschriften, Seriös aber gerne frische Farben bei einzelnen Elementen (z.B. bei Icons oder bei Handlungsaufforderungs-Buttons), Trennlinien, Inhalte auf den Punkt.
Logo-Entwurf anbei (wird gerade hier über entwurfhafen.de ebenfalls erstellt/optimiert, siehe #817306) sagt das wesentliche aus.
Kalendrio soll also ein sehr nützliches Tool sein, das jeder schnell versteht. Daher muss auch die Website sehr übersichtlich und klar aufgebaut werden. Die wesentlichen Aussagen/Menüpunkte finden sich auf der Startseite (bzw. im Hauptmenü, siehe grober Entwurf anbei).
- frische Farben (z.B. grün, orange, gelb)
- seröse Farben/Grauwerte (z.B. blau, grau, schwarz)
- Hauptmenü/Metanavigation/Footer-Bereich
Das Design und das Teaser-Bild (Frau mit Hammer) auf dem Entwurf anbei (seite1_mit_teaser_entwurf2.jpg) sind nur als grobe Ideen (Richtung) zu verstehen. Die Startseite muss also keine Teaser-Bilder enthalten.
Der Entwurf anbei soll lediglich die ungefähre Richtung mit den angedachten Menüpunkten verdeutlichen.
Übersichtlich und modern finden wir z.B. https://talkroomly.example/de (viel Weißraum, farbige Icons, Infos übersichtlich dargeboten, lächelnde Gesichter) und übrigens auch https://www.entwurfhafen.example.
Bitte entwerfen Sie (erstmal) drei Seiten:
- Startseite
- Funktionen/Preis (Beispiel auf https://talkroomly.example/de/tools Und/oder in Tabellenform wie auf https://talkroomly.example/de/pricing/ siehe Content-Plan anbei)
- Über Kalendrio (Über uns, siehe Content-Plan anbei)
Der Content-Plan soll das Projekt verdeutlichen.
Anmerkung von unserem Programmierer: Praktisch wäre eine Basis auf Bootstrap. Dies ist aber keine Pflicht! Das Design/die Idee geht vor :-)
1zu1-Folgeaufträge (für dieses und andere Projekte im Bereich Webdesign, Flyer, CorporateDesign, Grafiken) sind sehr wahrsc..

```html
<!DOCTYPE html>
<html lang="de">
<head>
<meta charset="utf-8">
<title>Kalendrio – Termine online managen</title>
<link rel="stylesheet" href="https://fonts.googleapis.com/css2?family=Roboto:wght@300;400;500;700&display=swap">
<style>
:root{
  --green:#86bc42;
  --green-dark:#76a936;
  --slate:#5d6b6b;
  --ink:#3f4747;
  --muted:#7c8585;
  --soft:#f5f5f5;
  --line:#e6e6e6;
  --white:#ffffff;
}
*{margin:0;padding:0;box-sizing:border-box}
html,body{width:698px;height:1200px;overflow:hidden;background:var(--white)}
body{position:relative;font-family:"Roboto",Arial,sans-serif;color:var(--ink)}
.abs{position:absolute}
a{color:inherit;text-decoration:none}

/* header */
.brand{left:38px;top:14px;display:flex;align-items:center;gap:5px;font-size:20px;font-weight:500;color:var(--slate)}
.brand-dot{width:14px;height:14px;border-radius:3px;background:var(--green)}
.meta-nav{top:5px;left:318px;display:flex;gap:14px;font-size:7.6px;color:var(--muted);font-weight:300}
.meta-nav span{display:flex;align-items:center;gap:3px}
.meta-nav i{display:block;width:9px;height:9px;border-radius:50%;border:1px solid var(--green)}
.lang{top:5px;left:634px;font-size:7.6px;color:var(--muted)}
.lang b{font-weight:500;color:var(--slate);border-bottom:1px solid var(--green)}
.main-nav{top:32px;left:352px;display:flex;gap:28px;font-size:8.6px;font-weight:500;color:var(--slate);letter-spacing:.2px}

/* hero */
.hero{left:0;top:53px;width:698px;height:300px;background:linear-gradient(100deg,#6f6a5f 0%,#4a4f4f 35%,#8d8a80 60%,#3f403c 100%)}
.hero-line{display:inline-block;background:rgba(95,107,107,.92);color:var(--white);padding:1px 6px;line-height:30px}
.hero-title{left:426px;top:148px;font-size:23px;font-weight:300}
.hero-title .hero-line:first-child{font-weight:700}
.arrow{left:12px;top:195px;width:14px;height:22px}
.arrow.right{left:672px}
.down{left:323px;top:327px;width:52px;height:26px;background:var(--white);border-radius:26px 26px 0 0}
.btn{display:flex;align-items:center;justify-content:center;background:var(--green);color:var(--white);font-size:6.4px;font-weight:500;letter-spacing:.2px;border-radius:13px}

/* intro */
.portrait{left:187px;top:388px;width:98px;height:98px;border-radius:50%;background:radial-gradient(circle at 50% 40%,#a19a92,#4d4b48 70%,#2d2c2a)}
.intro{left:298px;top:397px;width:230px;font-size:7.4px;line-height:11px;color:var(--slate);font-weight:300}
.intro h3{font-size:7.4px;font-weight:500;color:var(--ink);margin-bottom:6px}
.intro strong{font-weight:500;color:var(--ink)}
.intro .sig{margin-top:3px}

/* features */
.features{left:0;top:519px;width:698px;height:270px;background:var(--soft)}
.features h2{position:absolute;top:44px;width:100%;text-align:center;font-size:17px;font-weight:300;color:var(--slate)}
.feature{position:absolute;top:92px;width:104px;text-align:center}
.feature .ring{width:52px;height:52px;border:1px solid var(--slate);border-radius:50%;margin:0 auto 10px;display:flex;align-items:center;justify-content:center}
.feature h4{font-size:7.2px;font-weight:500;color:var(--ink);margin-bottom:1px}
.feature p{font-size:7.2px;line-height:11px;font-weight:300;color:var(--muted)}

/* devices */
.devices-art{left:0;top:789px;width:390px;height:220px;background:linear-gradient(135deg,#f7f7f7,#ececec 55%,#fafafa)}
.devices-copy{left:405px;top:840px;width:160px}
.mini-brand{display:flex;align-items:center;gap:3px;font-size:9px;font-weight:500;color:var(--slate)}
.mini-brand i{width:7px;height:7px;border-radius:2px;background:var(--green)}
.devices-copy h2{margin-top:9px;font-size:17px;line-height:21px;font-weight:300;color:var(--slate)}
.devices-copy h2 b{font-weight:500}
.devices-copy p{margin-top:12px;font-size:7.2px;line-height:11px;font-weight:300;color:var(--muted)}

/* footer */
.f-col{top:1051px;font-size:5.8px;color:var(--muted);font-weight:300}
.f-col h5{font-size:5.8px;font-weight:500;color:var(--ink);margin-bottom:10px}
.f-col li{list-style:none;line-height:11px}
.socials{left:445px;top:1068px;display:flex;gap:5px}
.socials i{width:17px;height:17px;border-radius:50%;background:var(--green)}
.hotline{left:445px;top:1106px;font-size:5.8px;font-weight:500;color:var(--ink)}
.hotline strong{display:block;margin-top:4px;font-size:9.2px;color:var(--slate)}
.rule{left:0;top:1157px;width:698px;height:1px;background:var(--line)}
.foot-brand{left:147px;top:1171px;display:flex;align-items:center;gap:3px;font-size:10px;color:var(--slate)}
.foot-brand i{width:6px;height:6px;border-radius:50%;background:var(--green)}
.copy{left:221px;top:1178px;font-size:5.6px;color:#aab0b0;font-weight:300}
.outline{display:flex;align-items:center;justify-content:center;border:1px solid var(--slate);border-radius:10px;font-size:6.2px;font-weight:500;color:var(--slate)}
</style>
</head>
<body>

<header>
  <div class="abs brand"><span class="brand-dot"></span>Kalendrio</div>
  <nav class="abs meta-nav">
    <span><i></i>Home</span><span><i></i>Login</span><span><i></i>Konto erstellen</span><span><i></i>Kontakt</span>
  </nav>
  <div class="abs lang"><b>DE</b> &nbsp;|&nbsp; EN</div>
  <nav class="abs main-nav">
    <a>FUNKTIONEN</a><a>PREISE</a><a>HELP-CENTER</a><a>ÜBER UNS</a><a>BLOG</a>
  </nav>
</header>

<section class="abs hero" role="img" aria-label="Foto: Hand hält ein Tablet mit Terminkalender, daneben eine Kaffeetasse"></section>
<svg class="abs arrow" viewBox="0 0 14 22"><path d="M12 2 3 11l9 9" fill="none" stroke="#fff" stroke-width="1.5"/></svg>
<svg class="abs arrow right" viewBox="0 0 14 22"><path d="M2 2l9 9-9 9" fill="none" stroke="#fff" stroke-width="1.5"/></svg>
<div class="abs hero-title">
  <span class="hero-line">Es ist an der Zeit,</span><br>
  <span class="hero-line">Termine online</span><br>
  <span class="hero-line">zu managen.</span>
</div>
<a class="abs btn" style="left:426px;top:261px;width:92px;height:24px">JETZT STARTEN!</a>
<div class="abs down"></div>
<svg class="abs" style="left:344px;top:341px" width="10" height="12" viewBox="0 0 10 12"><path d="M5 1v9M1.5 6.5 5 10l3.5-3.5" fill="none" stroke="#5d6b6b" stroke-width="1.3"/></svg>

<section>
  <div class="abs portrait" role="img" aria-label="Porträtfoto des Inhabers und Gründers"></div>
  <div class="abs intro">
    <h3>Kalendrio wurde aus der Not geboren.</h3>
    <p>„Wir benötigten selbst ein flexibles Tool, dass uns die <strong>lästige</strong> und <strong>zeitraubende</strong> Arbeit der <strong>Terminvereinbarung</strong> abnimmt.“</p>
    <p class="sig">Jonas Berger, Inhaber &amp; Gründer</p>
  </div>
  <a class="abs btn" style="left:298px;top:459px;width:92px;height:24px">MEHR INFOS</a>
</section>

<section class="abs features">
  <h2>Kalendrio hilft ihnen bei …</h2>
  <div class="feature" style="left:66px">
    <div class="ring"><svg width="30" height="30" viewBox="0 0 30 30"><rect x="3" y="6" width="22" height="19" rx="2" fill="none" stroke="#5d6b6b" stroke-width="2"/><path d="M3 11h22M9 3v6M19 3v6" stroke="#5d6b6b" stroke-width="2"/><circle cx="23" cy="23" r="6" fill="#fff" stroke="#5d6b6b" stroke-width="1.6"/><path d="M23 20v3h2.5" fill="none" stroke="#5d6b6b" stroke-width="1.4"/></svg></div>
    <h4>Terminvereinbarung</h4><p>Emporporepe alibercide et idendi dolupta tionsed qui sim eium aut mo comnien.</p>
  </div>
  <div class="feature" style="left:177px">
    <div class="ring"><svg width="30" height="30" viewBox="0 0 30 30"><rect x="6" y="16" width="5" height="8" fill="#5d6b6b"/><rect x="12" y="12" width="5" height="12" fill="#5d6b6b"/><rect x="18" y="6" width="5" height="18" fill="#5d6b6b"/><path d="M3 26h24" stroke="#5d6b6b" stroke-width="2"/></svg></div>
    <h4>Bewertungsmanagement</h4><p>Emporporepe alibercide et idendi dolupta tionsed qui sim eium aut mo comnien.</p>
  </div>
  <div class="feature" style="left:289px">
    <div class="ring"><svg width="30" height="30" viewBox="0 0 30 30"><path d="M5 11h6l12-7v20l-12-7H5z" fill="#5d6b6b"/><path d="M8 17l2 8h3l-1-8" fill="#5d6b6b"/></svg></div>
    <h4>Marketing</h4><p>Emporporepe alibercide et idendi dolupta tionsed qui sim eium aut mo comnien.</p>
  </div>
  <div class="feature" style="left:401px">
    <div class="ring"><svg width="30" height="30" viewBox="0 0 30 30"><circle cx="13" cy="8" r="5" fill="#5d6b6b"/><path d="M4 26c0-8 4-12 9-12s9 4 9 12z" fill="#5d6b6b"/><circle cx="22" cy="22" r="6" fill="#fff" stroke="#5d6b6b" stroke-width="1.5"/><path d="M22 19v6M19 22h6" stroke="#5d6b6b" stroke-width="1.4"/></svg></div>
    <h4>Kundengewinnung</h4><p>Emporporepe alibercide et idendi dolupta tionsed qui sim eium aut mo comnien.</p>
  </div>
  <div class="feature" style="left:512px">
    <div class="ring"><svg width="30" height="30" viewBox="0 0 30 30"><circle cx="13" cy="8" r="5" fill="#5d6b6b"/><path d="M4 26c0-8 4-12 9-12s9 4 9 12z" fill="#5d6b6b"/><circle cx="22" cy="22" r="6" fill="#fff" stroke="#5d6b6b" stroke-width="1.5"/><path d="M19 20.5h6l-2-2M25 23.5h-6l2 2" fill="none" stroke="#5d6b6b" stroke-width="1.2"/></svg></div>
    <h4>Kundenbindung</h4><p>Emporporepe alibercide et idendi dolupta tionsed qui sim eium aut mo comnien.</p>
  </div>
  <a class="btn" style="position:absolute;left:290px;top:215px;width:117px;height:24px">JETZT KONTO ERSTELLEN</a>
</section>

<section>
  <div class="abs devices-art" role="img" aria-label="Tablets und Smartphones mit Terminansichten auf hellem Grund"></div>
  <div class="abs devices-copy">
    <div class="mini-brand"><i></i>Kalendrio</div>
    <h2>Ihre Termine<br><b>immer</b> und<br><b>überall</b> im Blick.</h2>
    <p>Emporporepe alibercide et idendi dolupta tionsed qui sim eium aut mo comnien. Simus, voloresed et et etus cupta voluptiis et officto</p>
  </div>
</section>

<footer>
  <div class="abs f-col" style="left:147px"><h5>Preisübersicht</h5><ul><li>Termin-Assistent</li><li>Bewertungs-Tool</li><li>Besucher-Analyse</li><li>Statusmeldungen</li><li>Stornierungsfunktion</li><li>Filter-Tool</li></ul></div>
  <div class="abs f-col" style="left:221px"><h5>Top-Funktionen</h5><ul><li>Termin-Assistent</li><li>Bewertungs-Tool</li><li>Besucher-Analyse</li><li>Statusmeldungen</li><li>Stornierungsfunktion</li><li>Filter-Tool</li></ul></div>
  <div class="abs f-col" style="left:297px"><h5>Kalendrio</h5><ul><li>Kontakt</li><li>Über uns</li><li>Blog</li><li>Help-Center</li></ul></div>
  <div class="abs f-col" style="left:371px"><h5>Rechtliches</h5><ul><li>Sitemap</li><li>Impressum</li><li>Datenschutz</li></ul></div>
  <div class="abs f-col" style="left:445px"><h5>Folgen Sie uns bei</h5></div>
  <div class="abs socials"><i></i><i></i><i></i><i></i><i></i></div>
  <div class="abs hotline">Wir helfen Ihnen weiter<strong>0800 98765432</strong></div>
  <div class="abs rule"></div>
  <div class="abs foot-brand"><i></i>Kalendrio</div>
  <div class="abs copy">© 2018 Alle Rechte vorbehalten</div>
  <a class="abs outline" style="left:426px;top:1169px;width:47px;height:18px">LOGIN</a>
  <a class="abs outline" style="left:481px;top:1169px;width:63px;height:18px">DEUTSCH ▾</a>
</footer>

</body>
</html>
```